I needed some business cards done for my band. We are a 9 piece funk/horn band that plays a lot of private parties, wedding receptions and music festivals. We'd like a design with vivid colors that incorporates our logo. You can check out our website at www.brasslanternband.example to see what type of vibe we are going for.

```html
<!DOCTYPE html>
<html lang="en">
<head>
<meta charset="utf-8">
<title>Brass Lantern – Business Card</title>
<link rel="stylesheet" href="https://fonts.googleapis.com/css2?family=Poppins:wght@400;700&family=Lobster&display=swap">
<style>
  :root {
    --backdrop: #2e2e2e;
    --card: #0b0b0b;
    --lime: #c9dc2a;
    --white: #ffffff;
    --ink: #141414;
  }
  * { box-sizing: border-box; margin: 0; padding: 0; }
  html, body { width: 1200px; height: 866px; overflow: hidden; }
  body {
    background: var(--backdrop);
    font-family: "Poppins", sans-serif;
    position: relative;
  }
  .card {
    position: absolute;
    left: 320px;
    width: 560px;
    height: 320px;
    background: var(--card);
    box-shadow: 0 10px 24px rgba(0,0,0,.45);
    overflow: hidden;
  }
  .card--front { top: 83px; }
  .card--back { top: 463px; }

  .brand-name {
    position: absolute;
    color: var(--lime);
    font-weight: 700;
    letter-spacing: .5px;
    white-space: nowrap;
  }
  .card--front .brand-name { right: 40px; top: 62px; font-size: 38px; }
  .card--back .brand-name {
    left: 0; right: 0; top: 50%;
    transform: translateY(-50%);
    text-align: center;
    font-size: 54px;
  }

  .holder { position: absolute; left: 32px; top: 70px; }
  .holder__name {
    font-family: "Lobster", cursive;
    color: var(--lime);
    font-size: 24px;
    line-height: 1;
  }
  .holder__title { color: var(--white); font-size: 14px; margin-top: 2px; }

  .divider {
    position: absolute;
    left: 30px; right: 30px; top: 136px;
    height: 1px;
    background: var(--lime);
  }

  .contacts { position: absolute; left: 32px; top: 150px; list-style: none; }
  .contacts li {
    color: var(--white);
    font-size: 13px;
    display: flex;
    align-items: center;
    gap: 7px;
    line-height: 20px;
  }
  .contacts svg { width: 12px; height: 12px; fill: var(--lime); }

  .address {
    position: absolute;
    right: 32px; top: 196px;
    color: var(--white);
    font-size: 13px;
    line-height: 17px;
    text-align: right;
  }

  .band { position: absolute; left: 0; bottom: 0; width: 560px; height: 70px; }
  .band path, .band rect { fill: var(--lime); }
  .website {
    position: absolute;
    right: 32px; bottom: 27px;
    color: var(--ink);
    font-size: 14px;
  }
</style>
</head>
<body>
  <section class="card card--front">
    <div class="brand-name">Brass Lantern</div>

    <div class="holder">
      <div class="holder__name">Marcus Delaney</div>
      <div class="holder__title">Managing Director</div>
    </div>

    <div class="divider"></div>

    <ul class="contacts">
      <li>
        <svg viewBox="0 0 24 24" aria-hidden="true"><path d="M6.6 10.8a15 15 0 0 0 6.6 6.6l2.2-2.2c.3-.3.7-.4 1-.2 1.1.4 2.3.6 3.6.6.6 0 1 .4 1 1V20c0 .6-.4 1-1 1A17 17 0 0 1 3 4c0-.6.4-1 1-1h3.5c.6 0 1 .4 1 1 0 1.3.2 2.5.6 3.6.1.3 0 .7-.2 1z"/></svg>
        044-555 018 274
      </li>
      <li>
        <svg viewBox="0 0 24 24" aria-hidden="true"><path d="M2 5h20v14H2z M3 6l9 7 9-7" /></svg>
        info@brasslantern.example
      </li>
    </ul>

    <div class="address">421, Address line goes here<br>45452, Country Name</div>

    <svg class="band" viewBox="0 0 560 70" aria-hidden="true">
      <rect x="0" y="2" width="215" height="4"/>
      <path d="M0 14 H205 C228 14 228 -2 256 -2 H560 V50 H0 Z" transform="translate(0 10)"/>
    </svg>
    <div class="website">www.brasslanternband.example</div>
  </section>

  <section class="card card--back">
    <div class="brand-name">Brass Lantern</div>
  </section>
</body>
</html>
```